Business Card for Concrete supplier
Oak Lane Ready Mix
Business Card for Concrete supplier - Construction
Creative Brief
Simple
Marcel Dunham Jr.
President
P.O. Box 5172 Pearland, TX 77514
oaklanereadymix@mailnest.example
http://oaklanereadymix.example

```html
<!DOCTYPE html>
<html lang="en">
<head>
<meta charset="utf-8">
<title>Oak Lane Ready Mix — Business Card</title>
<link rel="stylesheet" href="https://fonts.googleapis.com/css2?family=Montserrat:wght@400;500;800&display=swap">
<style>
  :root {
    --backdrop: #d9d9d9;
    --card-dark: #3b3b3b;
    --stripe-white: #f7f7f7;
    --stripe-grey: #cfcfcf;
    --ink-light: #ffffff;
    --ink-soft: #c9c9c9;
  }
  * { box-sizing: border-box; margin: 0; padding: 0; }
  html, body {
    width: 1200px; height: 901px; overflow: hidden;
    background: var(--backdrop);
    font-family: "Montserrat", Arial, sans-serif;
  }
  .business-card {
    position: absolute; left: 75px; top: 150px;
    width: 1050px; height: 600px;
    display: flex;
    box-shadow: 0 6px 18px rgba(0,0,0,.18);
  }
  .card-face {
    position: relative;
    width: 865px; height: 100%;
    background: var(--card-dark);
    color: var(--ink-light);
    padding: 95px 0 0 105px;
  }
  .stripe-white { width: 110px; background: var(--stripe-white); }
  .stripe-grey { width: 75px; background: var(--stripe-grey); }

  .brand-name {
    font-weight: 800;
    font-size: 64px;
    letter-spacing: 1px;
    line-height: 1;
    text-transform: uppercase;
    color: var(--ink-light);
  }
  .tagline {
    margin-top: 18px;
    margin-left: 260px;
    font-size: 15px;
    color: var(--ink-soft);
    letter-spacing: 1px;
  }
  .person { position: absolute; left: 105px; top: 330px; }
  .person-name { font-size: 22px; font-weight: 500; }
  .person-title { font-size: 16px; color: var(--ink-soft); margin-top: 4px; }

  .address {
    position: absolute; left: 105px; top: 445px;
    font-size: 17px; line-height: 1.7;
  }
  .contacts {
    position: absolute; left: 375px; top: 445px;
    font-size: 17px; line-height: 1.7;
  }
  .contact-row { display: flex; align-items: center; gap: 12px; }
  .contact-row + .contact-row { margin-top: 2px; }
  .contact-row svg { width: 18px; height: 18px; flex: none; }
  .phone-pair { display: flex; gap: 30px; }
  .phone-pair .contact-row + .contact-row { margin-top: 0; }
</style>
</head>
<body>
  <section class="business-card">
    <div class="card-face">
      <h1 class="brand-name">Oak Lane Ready Mix</h1>
      <p class="tagline">Quality concrete delivered</p>

      <div class="person">
        <p class="person-name">Marcel Dunham Jr.</p>
        <p class="person-title">President</p>
      </div>

      <address class="address" style="font-style:normal">
        P.O. Box 5172<br>Pearland, TX 77514
      </address>

      <div class="contacts">
        <div class="phone-pair">
          <div class="contact-row">
            <svg viewBox="0 0 18 18" aria-hidden="true"><rect width="18" height="18" rx="2" fill="#fff"/><path d="M5 4h2.5l1 3-1.5 1a7 7 0 0 0 3 3l1-1.5 3 1V13a1 1 0 0 1-1 1A9 9 0 0 1 4 5a1 1 0 0 1 1-1z" fill="#3b3b3b"/></svg>
            <span>(281) 555-0147</span>
          </div>
          <div class="contact-row">
            <svg viewBox="0 0 18 18" aria-hidden="true"><rect width="18" height="18" rx="2" fill="#fff"/><rect x="4" y="7" width="10" height="6" fill="#3b3b3b"/><rect x="6" y="4" width="6" height="3" fill="#3b3b3b"/></svg>
            <span>(281) 555-0193</span>
          </div>
        </div>
        <div class="contact-row">
          <svg viewBox="0 0 18 18" aria-hidden="true"><rect width="18" height="18" rx="2" fill="#fff"/><rect x="3.5" y="5" width="11" height="8" fill="none" stroke="#3b3b3b" stroke-width="1.4"/><path d="M3.5 5l5.5 4.5L14.5 5" fill="none" stroke="#3b3b3b" stroke-width="1.4"/></svg>
          <span>oaklanereadymix@mailnest.example</span>
        </div>
        <div class="contact-row">
          <svg viewBox="0 0 18 18" aria-hidden="true"><rect width="18" height="18" rx="2" fill="#fff"/><circle cx="9" cy="9" r="5" fill="none" stroke="#3b3b3b" stroke-width="1.4"/><path d="M4 9h10M9 4c-2 3-2 7 0 10M9 4c2 3 2 7 0 10" fill="none" stroke="#3b3b3b" stroke-width="1.2"/></svg>
          <span>http://oaklanereadymix.example</span>
        </div>
      </div>
    </div>
    <div class="stripe-white"></div>
    <div class="stripe-grey"></div>
  </section>
</body>
</html>
```